Boutique raw honey label from Australia. Blue mountains clean environment

I need a quirky Eco label for a raw honey product to appeal to boutique honey buyers with Gm free 100% raw honey included. Honey come from blue mountains a world heritage listed area in nsw Aust.
Want to appeal to people who love good food and love beautiful things and who want to know where there food comes from and how it is grown. Gm free, pesticide free, hand poured family run and owned business

Target Market(s)

Health conscious, lovers of fine food

Industry/Entity Type

Environment

Other font styles liked:
• Courier

Requirements
Must have
• 100% Raw
Nice to have
• A little blurb about where honey is from
• # please see my current label - something similar to this but with a vintage bee design possibly

```html
<!DOCTYPE html>
<html lang="en">
<head>
<meta charset="UTF-8">
<title>Wattle Ridge Honey co. – Raw Honey Label</title>
<link rel="stylesheet" href="https://fonts.googleapis.com/css2?family=Special+Elite&family=Courier+Prime:wght@400;700&display=swap">
<style>
  :root {
    --page: #f2efe8;
    --label-black: #141414;
    --gold: #a8956a;
    --gold-line: #8a7a55;
    --honey-light: #f0c93a;
    --honey-deep: #c99d1c;
    --ink-light: #ebe8e1;
    --ink-muted: #c9c5bc;
  }
  * { box-sizing: border-box; margin: 0; padding: 0; }
  html, body {
    width: 900px;
    height: 1200px;
    overflow: hidden;
    background: var(--page);
  }
  .canvas {
    position: relative;
    width: 900px;
    height: 1200px;
  }
  .label {
    position: absolute;
    left: 60px;
    top: 255px;
    width: 780px;
    height: 690px;
    background: var(--label-black);
    box-shadow: 0 6px 24px rgba(0,0,0,0.18);
    color: var(--ink-light);
    font-family: "Courier Prime", "Courier New", monospace;
    overflow: hidden;
  }
  .label-art {
    position: absolute;
    inset: 0;
    width: 780px;
    height: 690px;
  }
  .brand-name {
    position: absolute;
    left: 80px;
    right: 80px;
    top: 108px;
    text-align: center;
    font-family: "Special Elite", "Courier New", monospace;
    font-weight: 400;
    font-size: 40px;
    line-height: 52px;
    color: var(--gold);
    letter-spacing: 0;
    white-space: nowrap;
  }
  .blurb {
    position: absolute;
    left: 40px;
    right: 40px;
    top: 184px;
    text-align: center;
    font-size: 20px;
    line-height: 44px;
    color: var(--ink-light);
    white-space: nowrap;
  }
  .blurb .raw-claim { font-size: 24px; }
  .blurb .percent { font-family: "Special Elite", "Courier New", monospace; font-size: 25px; }
  .blurb .place { font-weight: 700; }
  .claims-bar {
    position: absolute;
    left: 24px;
    right: 24px;
    top: 586px;
    display: flex;
    justify-content: space-between;
    align-items: center;
    font-size: 17px;
    color: var(--ink-muted);
  }
  .claims-free { display: flex; align-items: center; gap: 10px; }
  .claims-dot {
    width: 9px;
    height: 9px;
    border-radius: 50%;
    background: var(--gold-line);
  }
</style>
</head>
<body>
<main class="canvas">
  <section class="label">
    <svg class="label-art" viewBox="0 0 690 610">
      <g class="rule-lines" stroke="var(--gold-line)" stroke-width="1" stroke-dasharray="1.5 3" fill="none">
        <line x1="0" y1="18" x2="690" y2="18"/>
        <line x1="0" y1="45" x2="690" y2="45"/>
        <line x1="0" y1="552" x2="690" y2="552"/>
        <line x1="0" y1="580" x2="690" y2="580"/>
      </g>
      <g class="comb-frame" fill="none" stroke="var(--gold-line)" stroke-width="1.3">
        <polygon points="115,280 205.9,332.5 205.9,437.5 115,490 24.1,437.5 24.1,332.5"/>
        <polygon points="115,293 194.7,339 194.7,431 115,477 35.3,431 35.3,339" stroke-width="1"/>
        <polygon points="575,280 665.9,332.5 665.9,437.5 575,490 484.1,437.5 484.1,332.5"/>
        <polygon points="575,293 654.7,339 654.7,431 575,477 495.3,431 495.3,339" stroke-width="1"/>
        <polygon points="345,245 466.2,315 466.2,455 345,525 223.8,455 223.8,315" fill="var(--label-black)"/>
      </g>
      <defs>
        <linearGradient id="honeyFill" x1="0" y1="0" x2="1" y2="1">
          <stop offset="0" stop-color="var(--honey-light)"/>
          <stop offset="1" stop-color="var(--honey-deep)"/>
        </linearGradient>
      </defs>
      <polygon class="bee-emblem" role="img" aria-label="Vintage engraved honey bee on a golden honeycomb background"
        points="345,260 453.3,322.5 453.3,447.5 345,510 236.7,447.5 236.7,322.5"
        fill="url(#honeyFill)"/>
    </svg>

    <h1 class="brand-name">Wattle Ridge Honey co.</h1>

    <p class="blurb">
      <span class="raw-claim"><span class="percent">100%</span> raw honey</span> hand-poured in the<br>
      <span class="place">Blue Mountains</span> of New South Wales Australia.
    </p>

    <div class="claims-bar">
      <span class="claims-free">GM free <span class="claims-dot"></span> pesticide free</span>
      <span class="net-weight">Net wt. 430 gr</span>
    </div>
  </section>
</main>
</body>
</html>
```